New River III Precinct 6x11 GOTV postcard

We require BOTH persuasive copy and high-impact layout for an oversized 6x11 political mailer. This might be one person, but it likely requires a specialized "creative team." of an experienced political strategist copywriter PLUS a graphic designer - so the words fit the exact layout block, and the visuals reinforce the psychological punch of the headline.

The goal is to remove all excuses a targeted audience of ~900 registered Democratic + ~1800 Unaffiliated voters in our precinct - have for not voting.

I need to be able to work by phone / online chat to iterate designs
I need to own the design in the top couple of software outputs that any printer service will require.

I want to experiment with very subtle background images as follows:
- Front of postcard that conveys "CHANGE" of not just seasons - but of encouraging change of precinct voter representation - so anything about fall foliage / conveyance of change tie-in is worthy of considering
- Back of postcard - any Appalachian long rage mountain view that includes 5-7 layers of hills in the distance.
Some photos as samples to consider.

Target Market(s)

~2,700 registered Democrats and Unaffiliated voters

Requirements
Must have
• We require BOTH persuasive copy and high-impact layout for an oversized 6x11 political mailer. This might be one person, but it likely requires a specialized "creative team." of an experienced political strategist copywriter PLUS a graphic designer - so the words fit the exact layout block, and the visuals reinforce the psychological punch of the headline
Nice to have
• subtle background photos

```html
<!DOCTYPE html>
<html lang="en">
<head>
<meta charset="utf-8">
<title>New River III Precinct Postcard</title>
<link href="https://fonts.googleapis.com/css2?family=Oswald:wght@500;600&family=Roboto+Condensed:wght@400;700&display=swap" rel="stylesheet">
<style>
  :root {
    --page-bg: #e4e4e4;
    --card: #ffffff;
    --navy: #14204a;
    --navy-text: #1c2a5c;
    --red: #a11d24;
    --ink: #1d1d1d;
    --white: #ffffff;
    --shadow: 0 3px 10px rgba(0,0,0,0.18);
  }
  * { box-sizing: border-box; margin: 0; padding: 0; }
  html, body { width: 1200px; height: 1200px; overflow: hidden; }
  body {
    background: var(--page-bg);
    font-family: "Roboto Condensed", Arial, sans-serif;
    color: var(--ink);
    position: relative;
  }
  .postcard {
    position: absolute;
    left: 136px;
    width: 926px;
    height: 506px;
    background: var(--card);
    box-shadow: var(--shadow);
    overflow: hidden;
  }
  .postcard--front { top: 80px; }
  .postcard--back { top: 619px; }

  /* Front */
  .headline-bar {
    position: absolute;
    left: 0; top: 35px;
    width: 507px; height: 47px;
    background: var(--red);
    color: var(--white);
    font-family: "Oswald", Arial, sans-serif;
    font-weight: 600;
    font-size: 29px;
    line-height: 47px;
    padding-left: 42px;
  }
  .issues {
    position: absolute;
    left: 42px; top: 110px;
    width: 462px;
    font-size: 11px;
    line-height: 15px;
  }
  .issue { margin-bottom: 11px; }
  .issue--tight { margin-bottom: 0; }
  .issue-label, .cta { font-weight: 700; color: var(--navy-text); }

  .ballot-panel {
    position: absolute;
    left: 522px; top: 0;
    width: 292px; height: 100%;
    background: var(--navy);
  }
  .flag-art {
    position: absolute;
    left: 564px; top: 320px;
    width: 362px; height: 186px;
    background: linear-gradient(135deg, #3a4a8c 0%, #b8535a 55%, #d9a9ac 100%);
  }
  .ballot {
    position: absolute;
    left: 540px; top: 44px;
    width: 260px;
    color: var(--white);
    font-size: 11px;
    line-height: 13.5px;
    text-transform: uppercase;
  }
  .ballot-title { font-weight: 700; margin-bottom: 14px; }
  .race { margin-bottom: 14px; }
  .candidate { font-weight: 700; }
  .measure { font-weight: 700; margin-bottom: 14px; }

  /* Back */
  .flag-wash {
    position: absolute;
    left: 0; top: 130px;
    width: 200px; height: 376px;
    background: linear-gradient(160deg, rgba(200,60,70,0.12) 0%, rgba(255,255,255,0) 45%, rgba(40,60,140,0.10) 100%);
  }
  .letter {
    position: absolute;
    left: 42px; top: 44px;
    width: 515px;
    font-size: 11px;
    line-height: 15px;
  }
  .letter p { margin-bottom: 11px; }
  .salutation { font-weight: 700; color: var(--navy-text); margin-bottom: 8px !important; }
  .stamp-box {
    position: absolute;
    left: 757px; top: 47px;
    width: 107px; height: 124px;
    border: 1.5px solid var(--ink);
  }
  .voter-info {
    position: absolute;
    left: 42px; top: 308px;
    list-style: none;
    font-size: 11px;
    line-height: 20px;
    text-transform: uppercase;
  }
</style>
</head>
<body>

<section class="postcard postcard--front">
  <h1 class="headline-bar">VOTE FOR NEW REPRESENTATION</h1>

  <div class="issues">
    <p class="issue"><span class="issue-label">LOCAL PAIN-THANKS TO CURRENT REPRESENTATIVES</span> - and sadly, to avoid accountability, they've cleverly delayed many / most impacts until AFTER the 2026 election. <span class="cta">VOTE FOR CHANGE</span></p>
    <p class="issue"><span class="issue-label">FAMILY BUDGET:</span> exploded costs for everything; groceries, gas, car insurance, rent.</p>
    <p class="issue"><span class="issue-label">HEALTH</span> - expired subsidies, tax credits mean ~1m in NC will lose coverage or pay more. 50% cuts to Hospitals, Mental Health facilities; rural facilities will be closing</p>
    <p class="issue issue--tight"><span class="issue-label">REPRODUCTIVE RIGHTS</span> - Government authoritarian intrusion - censure women's rights.</p>
    <p class="issue issue--tight"><span class="issue-label">FOOD SECURITY</span> - Weaponized Hunger-cuts to SNAP; school meals cut; add'l work reqmts</p>
    <p class="issue"><span class="issue-label">EDUCATION</span> - Watauga $2.2mm shortfall personnel cuts, freezes in hiring, teacher training. Abandoning civil rights of Special Ed students to HHS and DOL</p>
    <p class="issue"><span class="issue-label">HOUSING</span> - 25% of renters are spending over 50% of income on rent. Especially bad locally; predatory leasing terms and skyrocketing rents. Proposed legislation is transforming HUD with the goal of getting rid of Section 8 housing that cares for vulnerable populations.</p>
    <p class="issue"><span class="issue-label">ENERGY</span> - In 2022 Boone achieved 100% renewable energy in town buildings; this is now being destroyed by repeal of renewable energy project funding; Ridge College Innovation District prepares renewable workforce technologies-all this is now in limbo.</p>
    <p class="issue"><span class="issue-label">ENVIRONMENT</span> - Reduced protections from coal ash pond leaks threaten public health. Corporations not held responsible for damage; public picks up the tab. Environmental Justice enforcement no longer a priority. Logging in Watauga with no public oversight. It's the "haz-mat" model do nothing, wait for catastrophe, then fix it</p>
  </div>

  <div class="ballot-panel"></div>
  <div class="flag-art" role="img" aria-label="Waving American flag"></div>

  <div class="ballot">
    <p class="ballot-title">Sample Ballot Recommendations</p>
    <p class="race">US Senate -<br><span class="candidate">Ray Colton</span></p>
    <p class="race">US House -District 5-<br><span class="candidate">Chet Hollis</span></p>
    <p class="measure">Reqmt to show ID for voters not in person-NO</p>
    <p class="race">State Senate District 47-<br><span class="candidate">Frank Hale</span></p>
    <p class="race">House of Rep's District 93-<br><span class="candidate">Carl Weston</span></p>
    <p class="race">NC Supreme Court<br><span class="candidate">Alma Evers</span></p>
    <p class="race">NC Court of Appeals-Seat 1<br><span class="candidate">Joel Ashby</span></p>
    <p class="race">NC Court of Appeals-Seat 2-<br><span class="candidate">Toby Harlan</span></p>
    <p class="race">NC Court of Appeals-Seat 3-<br><span class="candidate">Corinne Walsh</span></p>
  </div>
</section>

<section class="postcard postcard--back">
  <div class="flag-wash" role="img" aria-label="Faint waving flag background"></div>

  <div class="letter">
    <p class="salutation">Dear New River III Neighbor,</p>
    <p>We live in a representative democracy. We expect our representatives will exercise independent thinking and support policies and legislation that don't harm us - and that reflect the MAJORITY VIEWS of precinct citizens.</p>
    <p>But our current representatives HAVE STOPPED LISTENING - they are now bringing harmful policies straight to Watauga County. IT'S TIME TO HOLD THEM ACCOUNTABLE AND VOTE THEM OUT.</p>
    <p>Make no mistake: in 2026, every election is partisan. Even Judicial seats are now tied directly to state platforms.</p>
    <p>Any candidate who refuses to publicly condemn Raleigh's gerrymandered overreach into Watauga politics-or refuses to fight funding cuts for our healthcare, education, and environmental justice - is actively supporting these harmful policies.</p>
    <p>They are hoping their silence fools you. DON'T BE FOOLED. This November, VOTE FOR CHANGE.</p>
  </div>

  <div class="stamp-box"></div>

  <ul class="voter-info">
    <li>You are a registered voter in Watauga County</li>
    <li>You reside in precinct: New River III</li>
    <li>Polling places available to you are: Location,. 2, 3</li>
    <li>Early voting starts on:</li>
    <li>Deadline to apply for mail-in ballots</li>
    <li>Know the rules to ensure your mail-in-ballot counts</li>
  </ul>
</section>

</body>
</html>
```